We need a new design for our landing page. The baseline for the design should be our current landing page, that can be found on this page:
https://www.vorlani.com/convert/
We are quite open for making visual changes on this page. This means you have to respect the flow and the text, but all other components are up for a challenge if you feel that there are better ways of showing the page components.
The requirements are:
The page should be designed for computer view only.
The communication and the flow of the components on the current page must be unchanged.
The target group for the page is small and medium-sized business owners who have a website that generates some business to them (sales, contact collections etc.).They do not understand web analytics and are looking for an easy way to do so for them. Our solution helps them achieve this.
The challenge that we have with the current page is that the users do not discover how great our product is and how it actually can help them.
We provide an automated web analytics solution that tells them how to best improve their website.
This can be best illustrated with the attached page from our product. This tells you where to focus to improve your site's conversions.
We need this illustration to be a significant part of the top of the landing page, together with the wordings that are there already. Please note that this is not from a web-based dashboard, it is a page in a PDF report. This (current) text must be a part if the top of the page:"Vorlani is the automated web analytics PDF report, that lets you boost conversions by:Understanding why your users convertDriving converting traffic to your siteOptimising your navigation and engagementImprove your user flows."
It is ok if you have suggestions on how to do the last part of the landing page as well, but we are ok with that part of the flow.If you look at the other pages of our site, you will see that we try to make it clean and elegant, and this should be an aim for the landing page too.
We have a corporate colour pallet that I would like you to follow. The hex values are:
00C2E8
832926
027C74
036760
8FB1BC
The style we are looking for could be something like this:
https://pagebrisk.com/en-au/
Also we have e new project explainer video that you can include in stead of the "Know all your growth opportunities" section, It can be found on this page:
https://files.example-store.net/file/d/7Kq4TmZpW2xRb9LcNvH3yDfJ8sQa5EgU1/view
Finally. If you tink that there is too much information on the page, then it is ok for you to remove some components such as:
The world map
The benefits at a glance section
Web Analytics Out of the Box
Target Market(s)
Business owners from Small and medium sized business
Number of Pages Required
1 page

```html
<!DOCTYPE html>
<html lang="en">
<head>
<meta charset="utf-8">
<title>Vorlani – Web Analytics as a Service</title>
<link href="https://fonts.googleapis.com/css2?family=Oswald:wght@300;400;500;600;700&family=Roboto:wght@300;400;500;700&display=swap" rel="stylesheet">
<style>
:root{
  --teal-deep:#036760;
  --teal:#027C74;
  --cyan:#00C2E8;
  --wine:#832926;
  --slate:#8FB1BC;
  --ink:#1c2433;
  --muted:#5f6877;
  --line:#d9e3e6;
  --ghost:#eef2f3;
  --white:#ffffff;
}
*{box-sizing:border-box;margin:0;padding:0}
html,body{width:1200px;height:5373px;overflow:hidden}
body{position:relative;background:var(--white);font-family:'Roboto',sans-serif;color:var(--ink)}
.abs{position:absolute}
.heading{font-family:'Oswald',sans-serif;font-weight:600;text-transform:uppercase}
.btn{position:absolute;background:var(--wine);color:#fff;font-family:'Oswald',sans-serif;font-size:13px;letter-spacing:.5px;text-transform:uppercase;display:flex;align-items:center;justify-content:center;border-radius:2px}
.ph{position:absolute}

/* section titles */
.sec-title{position:absolute;left:0;width:1200px;text-align:center}
.sec-title .ghost{position:absolute;left:0;width:1200px;top:16px;font-family:'Oswald',sans-serif;font-weight:700;font-size:64px;color:var(--ghost);text-transform:uppercase;letter-spacing:2px;line-height:1}
.sec-title h2{position:relative;font-family:'Oswald',sans-serif;font-weight:600;font-size:22px;text-transform:uppercase;color:var(--ink);letter-spacing:.5px}
.sec-title .bar{position:relative;display:block;width:36px;height:2px;background:var(--ink);margin:8px auto 0}

/* hero */
.hero{position:absolute;left:0;top:0;width:1200px;height:660px;background:linear-gradient(180deg,var(--teal) 0%,var(--teal-deep) 100%)}
.nav-logo{position:absolute;left:60px;top:28px;display:flex;align-items:center;gap:10px;color:#fff;font-family:'Oswald',sans-serif;font-size:20px;letter-spacing:3px;font-weight:400}
.nav-logo i{display:block;width:26px;height:26px;border-radius:50%;border:2px solid #fff}
.nav-links{position:absolute;right:260px;top:40px;display:flex;gap:46px;color:#fff;font-family:'Oswald',sans-serif;font-size:13px;text-transform:uppercase}
.hero h1{position:absolute;left:130px;top:150px;width:470px;color:#fff;font-family:'Oswald',sans-serif;font-weight:600;font-size:44px;line-height:50px;text-transform:uppercase}
.hero .lead{position:absolute;left:130px;top:290px;width:440px;color:#fff;font-size:15px;line-height:22px;font-weight:500}
.ticks{position:absolute;left:130px;top:392px;width:500px;display:grid;grid-template-columns:250px 250px;row-gap:14px;color:#fff;font-size:12px;font-weight:500}
.ticks li{list-style:none;display:flex;align-items:center;gap:8px;white-space:nowrap}
.ticks svg{flex:none}

/* old & new */
.way-old{position:absolute;left:240px;top:830px;width:340px;text-align:center}
.way-new{position:absolute;left:590px;top:812px;width:370px;height:190px;background:var(--teal);color:#fff;text-align:center;padding-top:20px}
.way-title{font-family:'Oswald',sans-serif;font-weight:600;font-size:22px;text-transform:uppercase;color:var(--teal)}
.way-new .way-title{color:#fff}
.way-text{font-size:14px;line-height:20px;margin:14px auto 0;width:300px}

/* report band */
.report-band{position:absolute;left:0;top:1440px;width:1200px;height:650px;background:linear-gradient(180deg,var(--teal),var(--teal-deep))}
.report-band h2{position:absolute;left:160px;top:90px;width:420px;color:#fff;font-family:'Oswald',sans-serif;font-weight:600;font-size:36px;line-height:44px;text-transform:uppercase}
.report-band p{position:absolute;left:160px;top:340px;width:360px;color:#fff;font-size:14px;line-height:20px}
.circle-arrow{position:absolute;width:40px;height:40px;border-radius:50%;background:#fff;display:flex;align-items:center;justify-content:center}
.circle-arrow.ghosty{background:rgba(255,255,255,.35)}

/* growth */
.growth-text{position:absolute;left:215px;top:2345px;width:300px;font-size:14px;line-height:20px;color:var(--muted)}

/* services */
.svc{position:absolute;top:2740px;width:190px;text-align:center}
.svc .icon{width:64px;height:64px;border-radius:50%;margin:0 auto;background:radial-gradient(circle at 40% 40%,var(--cyan),var(--teal))}
.svc h3{margin-top:16px;font-family:'Oswald',sans-serif;font-size:13px;font-weight:600;color:var(--teal);text-transform:uppercase}
.svc p{margin-top:10px;font-size:10px;line-height:14px;color:var(--muted)}
.svc .more{margin:14px auto 0;width:62px;height:20px;background:var(--wine);color:#fff;font-size:9px;display:flex;align-items:center;justify-content:center;border-radius:2px}

/* newsletter */
.news{position:absolute;left:0;top:3080px;width:1200px;height:400px;background:var(--teal)}
.news .kicker{position:absolute;left:680px;top:72px;color:#fff;font-family:'Oswald',sans-serif;font-weight:300;font-size:22px;letter-spacing:2px;text-transform:uppercase}
.news h2{position:absolute;left:680px;top:104px;color:#fff;font-family:'Oswald',sans-serif;font-weight:600;font-size:44px;line-height:50px;text-transform:uppercase}
.field{position:absolute;background:#fff;height:34px;font-size:12px;color:var(--ink);display:flex;align-items:center;padding-left:12px;font-weight:500}

/* testimonials */
.quote{position:absolute;top:3735px;width:340px}
.quote .who{display:flex;align-items:center;gap:12px}
.quote .avatar{width:46px;height:46px;background:linear-gradient(135deg,#cfdde2,var(--slate))}
.quote .name{font-family:'Oswald',sans-serif;font-size:14px;font-weight:600}
.quote .role{font-size:10px;color:var(--muted)}
.quote p{margin-top:14px;font-size:11px;line-height:17px;color:var(--muted)}
.quote .mark{position:absolute;right:12px;top:188px;color:var(--wine);font-family:'Oswald',sans-serif;font-size:44px;line-height:1;font-weight:700}

/* pricing */
.plan{position:absolute;text-align:center;background:#fff;border:1px solid var(--line)}
.plan .pname{font-family:'Oswald',sans-serif;font-size:14px;font-weight:600;text-transform:uppercase;color:var(--teal);padding:18px 0 14px;border-bottom:1px solid var(--line)}
.plan .price{font-family:'Oswald',sans-serif;font-weight:600;font-size:48px;color:var(--teal);margin-top:18px;line-height:1}
.plan .per{font-size:13px;color:var(--muted);margin-top:4px}
.plan ul{list-style:none;margin-top:18px;font-size:12px;font-weight:600;line-height:24px;color:var(--ink);padding:0 10px}
.plan.featured{background:var(--teal);border:none;color:#fff}
.plan.featured .pname{background:var(--wine);color:#fff;border:none}
.plan.featured .price,.plan.featured .per,.plan.featured ul{color:#fff}

/* contact */
.contact{position:absolute;left:0;top:4700px;width:1200px;height:673px}
.contact .label{position:absolute;color:#fff;font-size:12px;font-weight:500}
.box{position:absolute;background:#fff}
.foot-links{position:absolute;left:0;top:5300px;width:1200px;display:flex;justify-content:center;gap:70px;color:#fff;font-size:12px;font-weight:500}
</style>
</head>
<body>

<header class="hero">
  <div class="nav-logo"><i></i>VORLANI</div>
  <nav class="nav-links"><span>Our Approach</span><span>Pricing</span><span>Testimonials</span></nav>
  <div class="btn" style="left:980px;top:32px;width:120px;height:30px">Get in touch</div>

  <h1>Welcome to web analytics as a service</h1>
  <p class="lead">Vorlani is the automated web analytics PDF report, that lets you boost conversions by:</p>
  <ul class="ticks">
    <li><svg width="14" height="14" viewBox="0 0 14 14"><path d="M2 7l3 3 7-7" stroke="#00C2E8" stroke-width="2" fill="none"/></svg>Understanding why your users convert</li>
    <li><svg width="14" height="14" viewBox="0 0 14 14"><path d="M2 7l3 3 7-7" stroke="#00C2E8" stroke-width="2" fill="none"/></svg>Driving converting traffic to your site</li>
    <li><svg width="14" height="14" viewBox="0 0 14 14"><path d="M2 7l3 3 7-7" stroke="#00C2E8" stroke-width="2" fill="none"/></svg>Optimising your navigation and engagement</li>
    <li><svg width="14" height="14" viewBox="0 0 14 14"><path d="M2 7l3 3 7-7" stroke="#00C2E8" stroke-width="2" fill="none"/></svg>Improve your user flows</li>
  </ul>
  <div class="btn" style="left:130px;top:480px;width:200px;height:34px">Download sample report</div>

  <div class="ph" role="img" aria-label="Page from the Vorlani PDF report showing where to focus to improve site conversions" style="left:660px;top:190px;width:440px;height:310px;background:linear-gradient(180deg,#ffffff,#e3ecef);box-shadow:0 8px 24px rgba(0,0,0,.28);border-top:6px solid var(--cyan)"></div>

  <svg class="abs" style="left:0;top:560px" width="1200" height="100" viewBox="0 0 1200 100" preserveAspectRatio="none">
    <path d="M0 60 C300 10 500 100 800 50 C1000 20 1120 40 1200 30 L1200 100 L0 100 Z" fill="#fff"/>
  </svg>
</header>

<div class="sec-title" style="top:712px"><div class="ghost">Old &amp; New Way</div><h2>Old &amp; New Way</h2><span class="bar"></span></div>

<div class="way-old">
  <div class="way-title">The old way</div>
  <p class="way-text" style="color:var(--muted)">A skilled web analytics expert analyse your website, so you could drive your business in a true data-driven way.</p>
</div>
<div class="way-new">
  <div class="way-title">The new way</div>
  <p class="way-text" style="font-weight:500">Vorlani is based on AI and mimics the tasks that a skilled analytics expert would have performed if he were to analyse your website</p>
</div>

<div class="ph" role="img" aria-label="Isometric illustration of an analyst at a desk and an automated report workflow" style="left:220px;top:1060px;width:760px;height:270px;background:linear-gradient(180deg,#f3f8f9,#cfe2e7)"></div>
<div class="btn" style="left:540px;top:1362px;width:120px;height:32px">Try for free</div>

<section class="report-band">
  <svg class="abs" style="left:0;top:0" width="1200" height="60" viewBox="0 0 1200 60" preserveAspectRatio="none"><path d="M0 0 L1200 0 L1200 20 C900 60 600 0 300 40 C150 55 60 40 0 30 Z" fill="#fff"/></svg>
  <h2>Vorlani is the smart web analytics report that identifies the best ways to your goals</h2>
  <p>Delivered to you as a beautifully designed and easy to understand PDF report</p>
  <div class="btn" style="left:160px;top:480px;width:200px;height:34px">Download sample report</div>

  <div class="ph" role="img" aria-label="PDF report page showing a focus diagram of connected goal circles and a data table" style="left:680px;top:140px;width:360px;height:280px;background:linear-gradient(180deg,#fdfdfd,#e3ecef);box-shadow:0 6px 20px rgba(0,0,0,.25)"></div>
  <div class="circle-arrow" style="left:580px;top:340px"><svg width="14" height="14" viewBox="0 0 14 14"><path d="M9 2L4 7l5 5" stroke="#036760" stroke-width="2.2" fill="none"/></svg></div>
  <div class="circle-arrow ghosty" style="left:1060px;top:340px"><svg width="14" height="14" viewBox="0 0 14 14"><path d="M5 2l5 5-5 5" stroke="#fff" stroke-width="2.2" fill="none"/></svg></div>

  <svg class="abs" style="left:0;top:590px" width="1200" height="60" viewBox="0 0 1200 60" preserveAspectRatio="none"><path d="M0 40 C250 0 500 60 800 30 C1000 10 1120 30 1200 20 L1200 60 L0 60 Z" fill="#fff"/></svg>
</section>

<div class="sec-title" style="top:2200px"><div class="ghost">Opportunities</div><h2>Know all your growth opportunities</h2><span class="bar"></span></div>
<div class="growth-text">
  <p>The Vorlani Report gives you a comprehensive overview of all your growth/improvement options. You get insights and recommendations you can act on and prioritise.</p>
  <p style="margin-top:14px">Last week, so you can focus on where it matters the most.</p>
</div>
<div class="btn" style="left:215px;top:2505px;width:110px;height:30px">Try for free</div>
<div class="ph" role="img" aria-label="Project explainer video shown on a laptop screen" style="left:640px;top:2330px;width:360px;height:250px;background:linear-gradient(135deg,#2f5f63,#0f2f33)"></div>
<svg class="abs" style="left:790px;top:2425px" width="60" height="60" viewBox="0 0 60 60"><circle cx="30" cy="30" r="27" fill="none" stroke="#fff" stroke-width="3"/><path d="M24 19 L41 30 L24 41 Z" fill="#fff"/></svg>

<div class="sec-title" style="top:2668px"><div class="ghost">Our Services</div><h2>Web analytics as a service</h2><span class="bar"></span></div>
<div class="svc" style="left:195px"><div class="icon" role="img" aria-label="Goal icon"></div><h3>Set up your goals</h3><p>You set up your goals with minimal effort and the tool maps how visitors reach them on your site.</p><div class="more">Read more</div></div>
<div class="svc" style="left:400px"><div class="icon" role="img" aria-label="Insight icon"></div><h3>Learn how your business</h3><p>Learn which pages, channels and journeys drive your results and where visitors drop.</p><div class="more">Read more</div></div>
<div class="svc" style="left:605px"><div class="icon" role="img" aria-label="Suggestions icon"></div><h3>Improvement suggestions</h3><p>Receive clear and prioritised suggestions on what to improve on your website next.</p><div class="more">Read more</div></div>
<div class="svc" style="left:810px"><div class="icon" role="img" aria-label="Changes icon"></div><h3>Implemented changes</h3><p>Track the changes you implemented and follow how your conversions develop over time.</p><div class="more">Read more</div></div>

<section class="news">
  <div class="ph" role="img" aria-label="Hands typing on a laptop showing an analytics dashboard" style="left:0;top:0;width:600px;height:400px;background:linear-gradient(135deg,#e6eef0,#a9c2c9 60%,#5d8088)"></div>
  <div class="kicker">Newsletter subscribe</div>
  <h2>Subscribe now<br>happy hour</h2>
  <div class="field" style="left:680px;top:222px;width:230px">Your Email</div>
  <div class="field" style="left:925px;top:222px;width:225px">Company Name</div>
  <div class="btn" style="left:680px;top:282px;width:130px;height:34px">Sign up Now</div>
</section>

<div class="sec-title" style="top:3625px"><div class="ghost">Testimonials</div><h2>What our clients say</h2><span class="bar"></span></div>
<svg class="abs" style="left:1090px;top:3690px" width="60" height="14" viewBox="0 0 60 14"><path d="M20 7H2M7 2L2 7l5 5" stroke="#1c2433" stroke-width="1.6" fill="none"/><path d="M40 7h18M53 2l5 5-5 5" stroke="#8FB1BC" stroke-width="1.6" fill="none"/></svg>

<div class="quote" style="left:-170px"><div class="who"><div class="avatar" role="img" aria-label="Client portrait"></div><div><div class="name">Dana Holt</div><div class="role">Webshop owner</div></div></div><p>Vorlani showed us exactly where our visitors dropped out. Within weeks we had changed our checkout and our conversion rate climbed steadily each month.</p><span class="mark">"</span></div>
<div class="quote" style="left:265px;width:300px"><div class="who"><div class="avatar" role="img" aria-label="Client portrait"></div><div><div class="name">Dana Holt</div><div class="role">Webshop owner</div></div></div><p>I never understood analytics before. The report tells me in plain words what to change, and I can finally act on my data without hiring an expert.</p><span class="mark">"</span></div>
<div class="quote" style="left:640px"><div class="who"><div class="avatar" role="img" aria-label="Client portrait"></div><div><div class="name">Dana Holt</div><div class="role">Webshop owner</div></div></div><p>The monthly PDF is clear and easy to share with my team. We used the suggestions to rework our navigation, and more visitors now reach our contact form. It saves us many hours every single month.</p><span class="mark">"</span></div>
<div class="quote" style="left:1020px"><div class="who"><div class="avatar" role="img" aria-label="Client portrait"></div><div><div class="name">Dana Holt</div><div class="role">Webshop owner</div></div></div><p>Great value for a small business. We know which channels bring buyers and stopped spending on the ones that did not.</p><span class="mark">"</span></div>

<div class="sec-title" style="top:4145px"><div class="ghost">Service Pricing</div><h2>Service pricing</h2><span class="bar"></span></div>
<div class="plan" style="left:230px;top:4230px;width:240px;height:330px"><div class="pname">Biggest pricing plan</div><div class="price">$125</div><div class="per">Charged Monthly</div><ul><li>One off Business Consults</li><li>Implement Quickly</li><li>Bump Trend Data</li><li>Plans and Results</li><li>Covers Multiply Technology Areas</li></ul></div>
<div class="plan featured" style="left:470px;top:4200px;width:260px;height:400px"><div class="pname">Premium pricing plan</div><div class="price">$250</div><div class="per">Monthly Service Charge</div><ul><li>Get Going Cost Control Strategy Practice</li><li>Freelance Contracts Management</li><li>Supplier Management Tips and Workshops</li><li>Advice and Guidance on Host Tiers on Your Site</li></ul></div>
<div class="plan" style="left:730px;top:4230px;width:240px;height:330px"><div class="pname">Ultimate pricing plan</div><div class="price">$349</div><div class="per">Charged Monthly</div><ul><li>One off Business Consults</li><li>Implement Quickly</li><li>Bump Trend Data</li><li>Plans and Results</li><li>Covers Multiply Technology Areas</li></ul></div>
<div class="btn" style="left:540px;top:4608px;width:120px;height:32px">Try for free</div>

<section class="contact">
  <div class="ph" role="img" aria-label="Faded city skyline over a teal backdrop" style="left:0;top:0;width:1200px;height:673px;background:linear-gradient(180deg,var(--teal),var(--teal-deep))"></div>
  <svg class="abs" style="left:0;top:0" width="1200" height="70" viewBox="0 0 1200 70" preserveAspectRatio="none"><path d="M0 0 L1200 0 L1200 20 C950 70 650 10 350 50 C200 65 80 50 0 40 Z" fill="#fff"/></svg>
  <h2 class="heading" style="position:absolute;left:0;top:108px;width:1200px;text-align:center;color:#fff;font-size:26px">Get in touch!</h2>
  <span style="position:absolute;left:582px;top:150px;width:36px;height:2px;background:#fff"></span>
  <span class="label" style="left:300px;top:186px">Name</span>
  <div class="box" style="left:300px;top:205px;width:300px;height:34px"></div>
  <span class="label" style="left:640px;top:186px">Email Address</span>
  <div class="box" style="left:640px;top:205px;width:300px;height:34px"></div>
  <span class="label" style="left:300px;top:260px">Your Message</span>
  <div class="box" style="left:300px;top:280px;width:640px;height:150px"></div>
  <div class="btn" style="left:820px;top:480px;width:120px;height:30px">Submit Now</div>

  <div style="position:absolute;left:340px;top:540px;color:#fff;font-size:12px;font-weight:500">hello@vorlani.com</div>
  <div style="position:absolute;left:555px;top:532px;display:flex;align-items:center;gap:8px;color:#fff;font-family:'Oswald',sans-serif;font-size:18px;letter-spacing:3px"><i style="display:block;width:22px;height:22px;border-radius:50%;border:2px solid #fff"></i>VORLANI</div>
  <div style="position:absolute;left:770px;top:540px;display:flex;align-items:center;gap:6px;color:#fff;font-size:12px;font-weight:500"><svg width="12" height="12" viewBox="0 0 12 12"><path d="M2 1h3l1 3-2 1c1 2 2 3 3 3l1-2 3 1v3c-5 1-10-4-9-9z" fill="#fff"/></svg>+1 555 0148</div>
</section>
<div class="foot-links"><span>Our Approach</span><span>Pricing</span><span>Testimonials</span><span>Get in touch</span></div>
<div style="position:absolute;left:0;top:5340px;width:1200px;text-align:center;color:#d6e6e8;font-size:10px">Copyright 2024 Vorlani. All rights reserved</div>
<div style="position:absolute;left:925px;top:5336px;display:flex;gap:8px">
  <i style="display:block;width:14px;height:14px;border-radius:50%;border:1.5px solid #fff"></i>
  <i style="display:block;width:14px;height:14px;border-radius:50%;border:1.5px solid #fff"></i>
  <i style="display:block;width:14px;height:14px;border-radius:50%;border:1.5px solid #fff"></i>
</div>

</body>
</html>
```